Lunavera Geist und Atem
Zielgruppe
Kosmetikbehandlungen für Sie und Ihn Medizinische Kosmetik, Ultraschall und Fruchtsäurebehandlungen und Hautschälkuren. Make up Artistic und Fußpflege so wie fernöstliche massagen. Die Bausteine Sind Kosmetikbehandlungen, Fernöstlichemassagen aus Hawaai und Bali so we Live Cotcing, Spirituellelebensberatung mit Kartenlegen.
Aufgabenstellung
Es ist nicht einfach was ich möchte. Schauen SIe sich meine Seite an www.stage.lunavera-beispiel.de
die werbeanzeige soll 13 mal 18 cm sein und es wird im Kräuterbund Oberfeld erscheinen, dort machen Heilpraktiker Lebensberater u.v.m. Werbung. Ich möchte das die Anzeige in den Farben von Lunavera weiß,grau, Orange gestaltet wird. Es soll auf mein Institut aufmerksam machen.
z.B Logo lunavera finden sie auf der webseite
Dann Gesundheit, Schönheit, Prävention und Innere Balance
Das Bild von mir welches Sie auf der Webseite sehen sollte auch mit in die Anzeig,e damit die Leute mich sehen können.
Dann der Text:
Tauchen Sie ein in die balinesische Behandlungsphilosophie von Lunavera Geist und Atem.
Dieser Ort umgeben von fließendem Wasser,naturbelassenen Wäldern und reiner klarer Luft zum Durchatmen, liegt mitten im Lindental bei Talheim. Ein Ort der Harmonie und Tiefenentspannung. Das Institut für professionelle Kosmetikbehandlungen, Fernöstliche Massagen sowie Ganzheitliche Lebensberatung und Kartenlegungen. Lassen Sie die Seele baumeln und bringen Sie Ihre Haut von Innen und Außen wieder zum Strahlen. Schönheit und innere Balance ist meine Berufung und diese bringe ich Ihnen Gerne nähe. Sind sie neugierig geworden? Seinen Sie offen und probieren Sie es aus. Und erleben Sie eine ganz besondere Art der Kosmetikbehandlung die viel Nachhaltigkeit mit sich bringt. Finden Sie Ruhe, kraft und kommen Sie wieder bei sich an. Ich bin gerne in allen Bereichen Proffesionel und einfühlsam für Sie da.
Herzliche Grüße
Entfalten Sie Ihre innere Schönheit und strahlen Sie mit viel Selbstbewusstsein und Lebensfreude.
Unser Angebot:
Beratung:
Kartenlegen mit Live-Coaching sowie
Kurzzeitberatungen und Mediale-Beratung.
Professionelle Kosmetikbehandlungen:
Kosmetikbehandlungen bei Problemhaut.
Fruchtsäurebehandlung und HautschÃ..

```html
<!DOCTYPE html>
<html lang="de">
<head>
<meta charset="utf-8">
<title>Lunavera Geist und Atem – Anzeige</title>
<link href="https://fonts.googleapis.com/css2?family=Crimson+Pro:wght@400;600;700&display=swap" rel="stylesheet">
<style>
  :root {
    --orange: #f07d00;
    --orange-light: #f7a333;
    --text: #3a3a3a;
    --grey: #6b6b6b;
    --green: #4c9a2a;
    --paper: #ffffff;
    --photo-bg: #d9cfc4;
    --photo-mid: #b89a82;
  }
  * { box-sizing: border-box; margin: 0; padding: 0; }
  html, body { width: 844px; height: 1200px; overflow: hidden; background: var(--paper); }
  body { font-family: "Crimson Pro", Georgia, serif; color: var(--text); position: relative; }
  .ad { position: absolute; inset: 0; background: var(--paper); }

  .brand { position: absolute; left: 40px; top: 82px; display: flex; align-items: center; gap: 14px; }
  .brand-dot { width: 22px; height: 22px; border-radius: 50%; background: var(--orange); }
  .brand-name { font-size: 74px; font-weight: 400; color: var(--orange); letter-spacing: 1px; line-height: 1; }

  .headline { position: absolute; left: 436px; top: 70px; width: 360px; font-size: 27px; font-weight: 700; line-height: 1.25; color: var(--orange); }

  .intro { position: absolute; left: 44px; top: 262px; width: 360px; font-size: 16.5px; line-height: 1.3; text-align: justify; hyphens: auto; -webkit-hyphens: auto; }
  .intro p { margin-bottom: 14px; }
  .intro .greeting { margin-bottom: 0; }
  .signature { width: 200px; height: 58px; margin-top: 4px; background: linear-gradient(90deg, #eeeeee, #f7f7f7); border-radius: 4px; }

  .offer { position: absolute; left: 446px; top: 250px; width: 340px; }
  .offer-title { font-size: 25px; font-weight: 700; color: var(--text); display: inline-block; }
  .offer-title svg { display: block; margin-top: -2px; }
  .offer-group { margin-top: 14px; }
  .offer-group h3 { font-size: 16.5px; font-weight: 700; color: var(--orange); margin-bottom: 6px; }
  .offer-group ul { list-style: none; }
  .offer-group li { position: relative; padding-left: 28px; font-size: 16.5px; line-height: 1.25; margin-bottom: 9px; }
  .offer-group li::before { content: ""; position: absolute; left: 6px; top: 8px; width: 6px; height: 6px; border-radius: 50%; background: var(--text); }

  .footer-band { position: absolute; left: 0; top: 940px; width: 844px; height: 260px; }

  .contact { position: absolute; left: 60px; top: 1040px; color: #fff; font-style: normal; font-weight: 700; font-size: 18px; line-height: 1.35; }
  .contact .gap { margin-top: 10px; }

  .portrait { position: absolute; left: 584px; top: 862px; width: 206px; height: 248px; background: var(--paper); padding: 6px; box-shadow: 0 2px 6px rgba(0,0,0,.25); transform: rotate(2deg); }
  .portrait-fill { width: 100%; height: 100%; background: linear-gradient(160deg, var(--photo-bg), var(--photo-mid) 70%, #9fb37a); }

  .tag { position: absolute; left: 403px; top: 900px; width: 164px; padding: 10px 12px; background: var(--green); color: #fff; font-weight: 700; font-size: 16.5px; line-height: 1.15; transform: rotate(-4deg); }
</style>
</head>
<body>
<main class="ad">
  <div class="brand">
    <span class="brand-dot"></span>
    <span class="brand-name">Lunavera</span>
  </div>

  <h1 class="headline">Entfalten Sie Ihre innere Schönheit und strahlen Sie mit viel Selbstbewusstsein und Lebensfreude.</h1>

  <section class="intro">
    <p>Tauchen Sie ein in die balinesische Behand&shy;lungs&shy;philosophie von Lunavera Geist und Atem.</p>
    <p>Dieser Ort umgeben von fließendem Wasser, naturbelassenen Wäldern und reiner klarer Luft zum Durchatmen, liegt mitten im Lindental bei Talheim. Ein Ort der Harmonie und Tiefen&shy;entspannung.</p>
    <p>Das Institut für professionelle Kosmetik&shy;behandlungen, Fernöstliche Massagen sowie Ganzheitliche Lebens&shy;beratung und Karten&shy;legungen. Lassen Sie die Seele baumeln und bringen Sie Ihre Haut von Innen und Außen wieder zum Strahlen. Schönheit und innere Balance ist meine Berufung und diese bringe ich Ihnen Gerne nähe. Sind sie neugierig geworden?</p>
    <p>Seinen Sie offen und probieren Sie es aus. Und erleben Sie eine ganz besondere Art der Kosmetik&shy;behandlung die viel Nachhaltig&shy;keit mit sich bringt. Finden Sie Ruhe, kraft und kommen Sie wieder bei sich an. Ich bin gerne in allen Bereichen Proffesionel und einfühlsam für Sie da.</p>
    <p class="greeting">Herzliche Grüße<br>Ihr</p>
    <div class="signature" role="img" aria-label="Handschriftliche Unterschrift von Jonas Werder"></div>
  </section>

  <section class="offer">
    <h2 class="offer-title">Unser Angebot
      <svg width="130" height="12" viewBox="0 0 130 12"><path d="M2 9 C40 2, 90 2, 128 6" stroke="var(--orange)" stroke-width="2.5" fill="none" stroke-linecap="round"/></svg>
    </h2>
    <div class="offer-group">
      <h3>Beratung:</h3>
      <ul><li>Kartenlegen mit Live-Coaching<br>sowie Kurzzeitberatungen<br>und Mediale-Beratung.</li></ul>
    </div>
    <div class="offer-group">
      <h3>Professionelle Kosmetikbehandlungen:</h3>
      <ul>
        <li>Kosmetikbehandlungen<br>bei Problemhaut.</li>
        <li>Fruchtsäurebehandlung und<br>Hautschälkuren.</li>
        <li>Make up Beratungen<br>und Schminkkurse.</li>
      </ul>
    </div>
    <div class="offer-group">
      <h3>Körperbehandlungen:</h3>
      <ul>
        <li>Hot Stone Massage Körper<br>und Gesicht.</li>
        <li>Bali Energetic Gesicht<br>und Körpermassage.</li>
        <li>Reikibehandlungen und<br>Edelsteinmassagen.</li>
        <li>Fußpflege.</li>
      </ul>
    </div>
  </section>

  <svg class="footer-band" viewBox="0 0 844 260" preserveAspectRatio="none" aria-hidden="true">
    <defs>
      <linearGradient id="bandFill" x1="0" y1="0" x2="0" y2="1">
        <stop offset="0" stop-color="var(--orange-light)"/>
        <stop offset="1" stop-color="var(--orange)"/>
      </linearGradient>
    </defs>
    <path d="M0 50 C220 0, 520 40, 844 90 L844 260 L0 260 Z" fill="url(#bandFill)"/>
    <path d="M0 70 C240 20, 520 60, 844 112" stroke="#fff" stroke-width="3" fill="none" opacity=".7"/>
  </svg>

  <address class="contact">
    <div>Lunavera Geist und Atem</div>
    <div>Kosmetikfachinstitut Jonas Werder</div>
    <div class="gap">Lindenhang 8 | 72999 Talheim-Oberau</div>
    <div>Tel: 07000 4815162</div>
    <div class="gap">info@lunavera.de | www.lunavera.de</div>
  </address>

  <figure class="portrait">
    <div class="portrait-fill" role="img" aria-label="Porträtfoto von Jonas Werder"></div>
  </figure>

  <div class="tag">Jonas Werder bekannt aus dem TV und Premium-parfümerien.</div>
</main>
</body>
</html>
```